Business Cards used to invite people to our church

We are a church and have need of a business card sized advertisement that allows our members to hand them out in order to invite people to the church. I need the front of the card to say "You're Invited" or "Come Check us out". with the service times on the back of the card later.
I have attached one of the OLD cards we have used in the past, but we want a complete makeover, into a more modern style that does not require the image.
I am also replacing the old logo with a newer "flat" logo which is attached.
Please use marketing colors. (blue or red or something that catches attention)
Create a card that DOES NOT have the picture of the two people on the front
The information on the sample card back is correct to go onto new card
Target Market(s)
anyone
Industry/Entity Type
Business
Contact Information for Business Card
sertice times and address information which you can get from the sample card I uploaded. It should have "You're Invited" or "Come Check us out" on the front of the card with out logo.

```html
<!DOCTYPE html>
<html lang="en">
<head>
<meta charset="utf-8">
<title>Grace Harbor Ministries – Invitation Card</title>
<link rel="stylesheet" href="https://fonts.googleapis.com/css2?family=Great+Vibes&family=PT+Sans:wght@400;700&family=Cinzel:wght@400&display=swap">
<style>
  :root {
    --page-bg: #e9e7e4;
    --card-red: #ff0000;
    --card-red-soft: #ff2a2a;
    --card-white: #ffffff;
    --ink-white: #ffffff;
    --shadow: rgba(0, 0, 0, 0.25);
  }
  * { box-sizing: border-box; margin: 0; padding: 0; }
  html, body {
    width: 1200px;
    height: 844px;
    overflow: hidden;
    background: var(--page-bg);
  }
  .sheet {
    width: 1200px;
    height: 844px;
    display: flex;
    align-items: center;
    justify-content: center;
    gap: 50px;
  }
  .card {
    position: relative;
    width: 540px;
    height: 310px;
    background: var(--card-white);
    box-shadow: 0 10px 30px var(--shadow);
    padding: 16px 0;
  }
  .card-field {
    position: relative;
    width: 100%;
    height: 100%;
    background: var(--card-red);
    overflow: hidden;
    color: var(--ink-white);
  }

  /* Front */
  .front-accent {
    position: absolute;
    left: 130px;
    top: -30px;
    width: 320px;
    height: 320px;
    border-radius: 50%;
    background: var(--card-red-soft);
  }
  .invite-title {
    position: absolute;
    left: 0;
    right: 0;
    top: 92px;
    text-align: center;
    font-family: "Great Vibes", cursive;
    font-weight: 400;
    font-size: 78px;
    line-height: 1;
    transform: rotate(-14deg);
    color: var(--ink-white);
  }

  /* Back */
  .service-times {
    position: absolute;
    left: 22px;
    top: 14px;
    width: 240px;
    list-style: none;
    font-family: "PT Sans", sans-serif;
    font-weight: 700;
    font-size: 11px;
    line-height: 16px;
  }
  .service-times li { display: flex; align-items: baseline; }
  .service-times .leader {
    flex: 1;
    border-bottom: 1px dotted var(--ink-white);
    margin: 0 2px;
    transform: translateY(-3px);
  }
  .brand {
    position: absolute;
    left: 0;
    right: 0;
    top: 110px;
    text-align: center;
  }
  .brand-dot {
    display: inline-block;
    width: 30px;
    height: 30px;
    border-radius: 50%;
    background: var(--ink-white);
    margin-bottom: 12px;
  }
  .brand-name {
    font-family: "Cinzel", serif;
    font-weight: 400;
    font-size: 21px;
    letter-spacing: 0.5px;
    color: var(--ink-white);
  }
  .contact-phone {
    position: absolute;
    right: 18px;
    top: 112px;
    display: flex;
    align-items: center;
    gap: 5px;
    font-family: "PT Sans", sans-serif;
    font-weight: 700;
    font-size: 11px;
  }
  .contact-address {
    position: absolute;
    left: 18px;
    bottom: 14px;
    display: flex;
    align-items: center;
    gap: 5px;
    font-family: "PT Sans", sans-serif;
    font-weight: 700;
    font-size: 12px;
  }
  .icon { width: 11px; height: 11px; fill: var(--ink-white); }
</style>
</head>
<body>
<main class="sheet">
  <section class="card card-front" aria-label="Card front">
    <div class="card-field">
      <div class="front-accent" aria-hidden="true"></div>
      <h1 class="invite-title">You're Invited</h1>
    </div>
  </section>

  <section class="card card-back" aria-label="Card back">
    <div class="card-field">
      <ul class="service-times">
        <li><span>Sunday</span><span class="leader"></span><span>9:00 Am</span></li>
        <li><span>Sunday</span><span class="leader"></span><span>11.00 Am</span></li>
        <li><span>Wed. Bible Class</span><span class="leader"></span><span>7:00 Pm</span></li>
      </ul>

      <div class="brand">
        <span class="brand-dot" aria-hidden="true"></span>
        <p class="brand-name">Grace Harbor Ministries</p>
      </div>

      <p class="contact-phone">
        <svg class="icon" viewBox="0 0 24 24" aria-hidden="true"><path d="M6.6 10.8a15.1 15.1 0 0 0 6.6 6.6l2.2-2.2c.3-.3.7-.4 1-.2 1.1.4 2.3.6 3.6.6.6 0 1 .4 1 1V20c0 .6-.4 1-1 1C10.6 21 3 13.4 3 4c0-.6.4-1 1-1h3.5c.6 0 1 .4 1 1 0 1.3.2 2.5.6 3.6.1.3 0 .7-.2 1z"/></svg>
        1-800-555-0142
      </p>

      <p class="contact-address">
        <svg class="icon" viewBox="0 0 24 24" aria-hidden="true"><path d="M12 2a7 7 0 0 0-7 7c0 5.3 7 13 7 13s7-7.7 7-13a7 7 0 0 0-7-7zm0 9.5A2.5 2.5 0 1 1 12 6.5a2.5 2.5 0 0 1 0 5z"/></svg>
        2480 Cedar Lane - Fairview, Tx 75069
      </p>
    </div>
  </section>
</main>
</body>
</html>
```